sydney wedding photography business needs a business card design

we need a business card design for a sydney based wedding photography and videography business. our business name is :golden hour photography and video. our target clients are 24-35 yrs female. our style is candid, organic, natural, dynamic. we are a team of young photographers and videographers, and help brides to create memories that they will cherish for the rest of their lives. the logo will be provided. we want an elegant design that reflects our style, and also want to give a great impression to our clients that we are one of the best studios in sydney and our brand means quality and premium service.

Target Market(s)

bride to be, 24-35 years old, living in sydney and surrunding areas

Industry/Entity Type

Wedding Photography

Contact Information for Business Card

address: 57 marrow lane, bexton nsw 2041
mobile: 0431872056
phone: (02) 9361 2748
info@goldenhourstudio.net.au
www.goldenhourstudio.net.au
facebook:goldenhourbridals
instagram:goldenhourbridals

Font styles to use
Serif
Sans Serif

Requirements
Nice to have
• maybe add my slogan"memories beyond eternity" if the layout looks good
Should not have
• no black color, not good idea for wedding biz card

```html
<!DOCTYPE html>
<html lang="en">
<head>
<meta charset="utf-8">
<title>Golden Hour – Business Card</title>
<link rel="stylesheet" href="https://fonts.googleapis.com/css2?family=Roboto:wght@400;500&display=swap">
<style>
  :root {
    --backdrop: #e9e4dc;
    --gold-light: #d8a23a;
    --gold-mid: #b9801f;
    --gold-deep: #8a5510;
    --ink: #2a1c0b;
    --cocoa-light: #4e3218;
    --cocoa-deep: #24160a;
    --rim: #a89a86;
    --logo-gold: #e2ad4c;
  }
  html, body {
    margin: 0;
    width: 1200px;
    height: 969px;
    overflow: hidden;
    background: var(--backdrop);
  }
  .canvas {
    position: relative;
    width: 1200px;
    height: 969px;
  }
  .card {
    position: absolute;
    left: 100px;
    top: 200px;
    width: 1000px;
    height: 570px;
    overflow: hidden;
    box-shadow: 0 18px 40px rgba(60, 40, 10, 0.25);
    background: radial-gradient(ellipse at 30% 40%, var(--gold-light) 0%, var(--gold-mid) 45%, var(--gold-deep) 100%);
    font-family: "Roboto", Arial, sans-serif;
    color: var(--ink);
  }
  .card-art {
    position: absolute;
    inset: 0;
  }
  .person {
    position: absolute;
    left: 47px;
    top: 42px;
  }
  .person-name {
    margin: 0;
    font-size: 32px;
    font-weight: 500;
    line-height: 1.1;
  }
  .person-role {
    margin: 4px 0 0;
    font-size: 25px;
    font-weight: 400;
  }
  .address {
    position: absolute;
    left: 47px;
    top: 206px;
    margin: 0;
    font-style: normal;
    font-size: 23px;
    line-height: 35px;
  }
  .contacts {
    position: absolute;
    left: 47px;
    top: 288px;
    margin: 0;
    padding: 0;
    list-style: none;
    font-size: 23px;
  }
  .contacts li {
    display: flex;
    align-items: center;
    height: 38px;
    white-space: nowrap;
  }
  .contact-icon {
    width: 22px;
    height: 22px;
    margin-right: 14px;
    flex: none;
    fill: var(--ink);
  }
  .brand {
    position: absolute;
    left: 732px;
    top: 286px;
    transform: translate(-50%, -50%);
    margin: 0;
    font-family: "Roboto", Arial, sans-serif;
    font-size: 56px;
    font-weight: 500;
    color: var(--logo-gold);
    white-space: nowrap;
  }
</style>
</head>
<body>
<main class="canvas">
  <section class="card" aria-label="Business card">
    <svg class="card-art" width="1000" height="570" viewBox="0 0 1000 570" aria-hidden="true">
      <defs>
        <radialGradient id="cocoa-fill" cx="0.35" cy="0.5" r="0.7">
          <stop offset="0" stop-color="var(--cocoa-light)"/>
          <stop offset="1" stop-color="var(--cocoa-deep)"/>
        </radialGradient>
      </defs>
      <circle class="lens-rim" cx="740" cy="286" r="318" fill="var(--rim)"/>
      <circle class="lens-face" cx="740" cy="286" r="305" fill="url(#cocoa-fill)"/>
    </svg>

    <header class="person">
      <h1 class="person-name">Liam Carter</h1>
      <p class="person-role">President</p>
    </header>

    <address class="address">57 marrow lane<br>bexton nsw 2041</address>

    <ul class="contacts">
      <li>
        <svg class="contact-icon" viewBox="0 0 24 24" aria-hidden="true"><path d="M3 8c0-2 4-4 9-4s9 2 9 4v2h-5V8H8v2H3zM6 11h12l3 9H3z"/></svg>
        (02) 9361 2748
      </li>
      <li>
        <svg class="contact-icon" viewBox="0 0 24 24" aria-hidden="true"><path d="M7 1h10a2 2 0 0 1 2 2v18a2 2 0 0 1-2 2H7a2 2 0 0 1-2-2V3a2 2 0 0 1 2-2zm0 3v14h10V4zm5 15.5a1.2 1.2 0 1 0 0 2.4 1.2 1.2 0 0 0 0-2.4z"/></svg>
        (04) 3187 2056
      </li>
      <li>
        <svg class="contact-icon" viewBox="0 0 24 24" aria-hidden="true"><path d="M2 6h20v13H2zm2 2v.4l8 5 8-5V8l-8 5z"/></svg>
        info@goldenhourstudio.net.au
      </li>
      <li>
        <svg class="contact-icon" viewBox="0 0 24 24" aria-hidden="true"><circle cx="12" cy="12" r="10"/><path d="M2 12h20M12 2c3 3 3 17 0 20M12 2c-3 3-3 17 0 20" stroke="#c48a2a" stroke-width="1.5" fill="none"/></svg>
        www.goldenhourstudio.net.au
      </li>
      <li>
        <svg class="contact-icon" viewBox="0 0 24 24" aria-hidden="true"><circle cx="12" cy="12" r="10"/></svg>
        goldenhourbridals
      </li>
      <li>
        <svg class="contact-icon" viewBox="0 0 24 24" aria-hidden="true"><circle cx="12" cy="12" r="10"/></svg>
        goldenhourbridals
      </li>
    </ul>

    <p class="brand">Golden Hour</p>
  </section>
</main>
</body>
</html>
```